Freelance Makeup Artist Needing Business Card Design

I am a freelance makeup artist looking for a design for my business cards.
My target audience is people looking for bridal makeup, so i was thinking minimalistic style, black with white or gold foil accents.
Something that feels classy but simple and to the point.

I would like the front to state Naomi Carrow and Makeup Artist, and the back to include my social media and contact details.

Target Market(s)

Brides, young women

Industry/Entity Type

Business

Contact Information for Business Card

0417293846
naomi.carrow@mailvista.com
www.snapgrid.com/naomi.carrow
www.friendpage.com/NaomiCarrowMakeup

Requirements
Nice to have
• Social media icons next to relevant contact details

```html
<!DOCTYPE html>
<html lang="en">
<head>
<meta charset="utf-8">
<title>Naomi Carrow – Makeup Artist Business Card</title>
<link href="https://fonts.googleapis.com/css2?family=Jost:wght@300;400;600&display=swap" rel="stylesheet">
<style>
  :root {
    --backdrop: #2b2621;
    --card-base: #16191f;
    --card-shade: #0d0f13;
    --gold-light: #f3dd8a;
    --gold-mid: #c9a043;
    --gold-deep: #8a6521;
    --ivory: #f2f0ec;
    --rule: #b9b4a8;
  }
  * { margin: 0; padding: 0; box-sizing: border-box; }
  html, body {
    width: 1200px;
    height: 900px;
    overflow: hidden;
    background: var(--backdrop);
    font-family: "Jost", sans-serif;
  }
  .sheet {
    width: 1200px;
    height: 900px;
    display: flex;
    flex-direction: column;
    align-items: center;
    justify-content: center;
    gap: 60px;
  }
  .card {
    position: relative;
    width: 640px;
    height: 366px;
    background:
      radial-gradient(ellipse at 30% 20%, rgba(255,255,255,0.05), transparent 60%),
      linear-gradient(160deg, var(--card-base), var(--card-shade));
    box-shadow: 0 18px 40px rgba(0,0,0,0.55);
    font-variant: small-caps;
  }
  .gold-foil {
    background: linear-gradient(180deg, var(--gold-light) 0%, var(--gold-mid) 55%, var(--gold-deep) 100%);
    -webkit-background-clip: text;
    background-clip: text;
    color: transparent;
  }
  /* Front */
  .card-front .identity {
    position: absolute;
    left: 50%;
    top: 50%;
    transform: translate(-50%, -55%);
    text-align: center;
  }
  .card-front .name {
    font-size: 52px;
    font-weight: 600;
    letter-spacing: 1px;
    line-height: 1.05;
    white-space: nowrap;
  }
  .card-front .divider {
    height: 1px;
    margin: 6px 0 6px;
    background: linear-gradient(90deg, transparent, var(--rule) 10%, var(--rule) 90%, transparent);
  }
  .card-front .role {
    font-size: 24px;
    font-weight: 300;
    letter-spacing: 2px;
    color: var(--gold-mid);
  }
  /* Back */
  .card-back .block {
    position: absolute;
    left: 118px;
    top: 92px;
    width: 400px;
  }
  .card-back .rule-top {
    height: 1px;
    width: 300px;
    margin-left: -40px;
    background: var(--rule);
  }
  .card-back .name {
    font-size: 48px;
    font-weight: 600;
    letter-spacing: 1px;
    line-height: 1.1;
    margin: 6px 0 0 20px;
    white-space: nowrap;
  }
  .card-back .name .first { color: var(--ivory); }
  .card-back .rule-bottom {
    height: 1px;
    width: 380px;
    margin: 4px 0 10px 60px;
    background: var(--rule);
  }
  .contact {
    list-style: none;
    text-align: right;
    font-weight: 400;
    font-size: 17px;
    line-height: 1.45;
    color: var(--ivory);
  }
  .contact .phone {
    letter-spacing: 9px;
    font-weight: 300;
    font-size: 20px;
    color: var(--ivory);
  }
  .contact .social-page { color: var(--gold-mid); }
</style>
</head>
<body>
  <main class="sheet">
    <section class="card card-front" aria-label="Business card front">
      <div class="identity">
        <h1 class="name gold-foil">Naomi Carrow</h1>
        <div class="divider"></div>
        <p class="role">Makeup Artist</p>
      </div>
    </section>

    <section class="card card-back" aria-label="Business card back">
      <div class="block">
        <div class="rule-top"></div>
        <h2 class="name"><span class="first">Naomi</span> <span class="gold-foil">Carrow</span></h2>
        <div class="rule-bottom"></div>
        <ul class="contact">
          <li class="phone">0417293846</li>
          <li class="email">naomi.carrow@mailvista.com</li>
          <li class="social">www.snapgrid.com/naomi.carrow</li>
          <li class="social-page">www.friendpage.com/NaomiCarrowMakeup</li>
        </ul>
      </div>
    </section>
  </main>
</body>
</html>
```